Tradewell Banner Design for B2B Consulting Firm

Take the already developed logo (attached) and incorporate it into a creative banner design for placement on Tradewell (the social media platform targeting business users). The banner will be used on the firm's company profile page on Tradewell (not yet created).

```html
<!DOCTYPE html>
<html lang="en">
<head>
<meta charset="utf-8">
<title>Cedarline Advisors – Tradewell Banner</title>
<link href="https://fonts.googleapis.com/css2?family=Caladea&display=swap" rel="stylesheet">
<style>
  :root {
    --forest: #46644d;
    --moss: #6a8468;
    --sage: #9ab08b;
    --sage-soft: #b7c7a9;
    --ivory: #f4f5ee;
    --paper: #ffffff;
    --coin: #f2b233;
  }
  * { margin: 0; padding: 0; box-sizing: border-box; }
  html, body {
    width: 1200px;
    height: 448px;
    overflow: hidden;
    background: var(--paper);
    font-family: "Caladea", Cambria, Georgia, serif;
  }
  .canvas { position: relative; width: 1200px; height: 448px; }

  .banner {
    position: absolute;
    left: 74px; top: 91px;
    width: 1068px; height: 181px;
    background: var(--forest);
  }
  .banner__band-mid {
    position: absolute; left: 0; top: 155px;
    width: 100%; height: 15px;
    background: var(--moss);
  }
  .banner__band-light {
    position: absolute; left: 0; top: 170px;
    width: 100%; height: 11px;
    background: var(--sage);
  }

  .brand-card {
    position: absolute;
    left: 111px; top: 169px;
    width: 157px; height: 147px;
    background: var(--paper);
    box-shadow: 0 3px 5px rgba(0,0,0,0.28);
    display: flex; flex-direction: column;
    align-items: center; justify-content: center;
    gap: 12px;
  }
  .brand-card__square {
    width: 22px; height: 22px;
    background: var(--forest);
  }
  .brand-card__name {
    color: var(--forest);
    font-size: 19px;
    line-height: 1.1;
    text-align: center;
  }

  .tagline {
    position: absolute;
    left: 351px; top: 145px;
  }
  .tagline__rule {
    width: 83px; height: 3px;
    border-radius: 2px;
    background: var(--sage);
    margin-bottom: 7px;
  }
  .tagline__lead,
  .tagline__follow {
    font-size: 23.5px;
    line-height: 28px;
    white-space: nowrap;
  }
  .tagline__lead { color: var(--ivory); }
  .tagline__follow { color: var(--sage); }

  .money-art {
    position: absolute;
    left: 898px; top: 192px;
    width: 88px; height: 55px;
    border-radius: 6px;
    background: linear-gradient(120deg, var(--coin) 0%, var(--coin) 22%, #8fa486 30%, #7d9377 100%);
  }

  .growth-chart {
    position: absolute;
    left: 970px; top: 105px;
    width: 140px; height: 142px;
  }
</style>
</head>
<body>
<div class="canvas">
  <div class="banner">
    <div class="banner__band-mid"></div>
    <div class="banner__band-light"></div>
  </div>

  <div class="tagline">
    <div class="tagline__rule"></div>
    <p class="tagline__lead">Elevate your B2B success with strategic consulting</p>
    <p class="tagline__follow">that turns opportunities into triumphs</p>
  </div>

  <div class="money-art" role="img" aria-label="Illustration of a banded stack of banknotes with gold coins"></div>

  <svg class="growth-chart" viewBox="970 105 140 142" aria-label="Rising bar chart with upward trend arrow">
    <defs>
      <linearGradient id="barShade" x1="0" y1="0" x2="1" y2="0">
        <stop offset="0" stop-color="#9ab08b"/>
        <stop offset="1" stop-color="#87a07b"/>
      </linearGradient>
    </defs>
    <g fill="url(#barShade)">
      <rect x="978" y="168" width="18" height="79"/>
      <rect x="1002" y="135" width="18" height="112"/>
      <rect x="1027" y="151" width="18" height="96"/>
      <rect x="1051" y="109" width="18" height="138"/>
      <rect x="1073" y="139" width="18" height="108"/>
    </g>
    <polyline points="984,211 998,191 1016,221 1043,155 1060,186 1097,121"
              fill="none" stroke="#ffffff" stroke-width="3.5" stroke-linejoin="miter"/>
    <polygon points="1103,111 1102,127 1096,121 1089,118" fill="#ffffff"/>
  </svg>

  <div class="brand-card">
    <div class="brand-card__square"></div>
    <p class="brand-card__name">Cedarline<br>Advisors</p>
  </div>
</div>
</body>
</html>
```